New Business Card

We need to refresh our business cards. We designed these ourselves and we have no graphic design experience. We would like to find a new business card design that is professional and unique. We are an auto finance company. Feel free to play with the logo, but we would like to keep the eye very present on the card. Our corporate colors are green, grey, and white.
Green - RGB - 168,215,27; HEX - #AADD22
Grey - RGB - 196,196,196; HEX - #C4C4C4
Updates
Need to upload the vector file to finalize the project. The last logo was for a jpeg that didn't stretch well.
Industry/Entity Type
Financial Service
Contact Information for Business Card
Honestly don't know...I need your help!

```html
<!DOCTYPE html>
<html lang="en">
<head>
<meta charset="utf-8">
<title>Brightlane Capital — Business Card</title>
<link rel="stylesheet" href="https://fonts.googleapis.com/css2?family=Oxygen:wght@400;700&family=Lora:wght@400;700&display=swap">
<style>
  :root {
    --stage: #1f1f1f;
    --card-grey: #6e6e6e;
    --card-white: #ffffff;
    --brand-green: #a3cf3a;
    --brand-grey: #c4c4c4;
    --text-grey: #a9a9a9;
    --ink-white: #ffffff;
  }
  * { margin: 0; padding: 0; box-sizing: border-box; }
  html, body { width: 1200px; height: 1189px; overflow: hidden; }
  body {
    background: var(--stage);
    position: relative;
    font-family: "Lora", Georgia, serif;
  }
  .card {
    position: absolute;
    left: 170px;
    width: 860px;
    height: 491px;
    border-radius: 34px;
    overflow: hidden;
  }
  /* Back of card */
  .card--back { top: 60px; background: var(--card-grey); }
  .brand-lockup {
    position: absolute;
    display: flex;
    align-items: center;
    gap: 16px;
    font-family: "Oxygen", Arial, sans-serif;
    font-weight: 700;
  }
  .card--back .brand-lockup {
    left: 0; right: 0; top: 170px;
    justify-content: center;
    color: var(--ink-white);
    font-size: 54px;
  }
  .brand-dot {
    width: 30px; height: 30px; border-radius: 50%;
    background: currentColor;
    flex: none;
  }
  .card--back .web-address {
    position: absolute;
    left: 0; right: 0; top: 330px;
    text-align: center;
    color: var(--ink-white);
    font-size: 20px;
    letter-spacing: 5px;
  }
  /* Front of card */
  .card--front { top: 640px; background: var(--card-white); }
  .name-tab {
    position: absolute;
    left: -22px; top: 66px;
    width: 44px; height: 44px;
    border-radius: 50%;
    background: var(--brand-green);
  }
  .person {
    position: absolute;
    left: 50px; top: 60px;
  }
  .person-name {
    color: var(--brand-green);
    font-weight: 700;
    font-size: 28px;
    line-height: 1;
  }
  .person-role {
    color: var(--text-grey);
    font-size: 20px;
    margin-top: 2px;
  }
  .card--front .brand-lockup {
    right: 56px; top: 110px;
    color: var(--brand-green);
    font-size: 44px;
  }
  .address {
    position: absolute;
    right: 60px; top: 300px;
    text-align: right;
    color: var(--text-grey);
    font-size: 20px;
    line-height: 1.35;
  }
  .contact-list {
    position: absolute;
    left: 100px; bottom: 50px;
    list-style: none;
    color: var(--text-grey);
    font-size: 22px;
  }
  .contact-list li {
    display: flex; align-items: center; gap: 14px;
    height: 34px;
  }
  .contact-icon { width: 26px; height: 26px; flex: none; }
</style>
</head>
<body>
  <section class="card card--back" aria-label="Card back">
    <div class="brand-lockup"><span class="brand-dot"></span><span>Brightlane Capital</span></div>
    <p class="web-address">www.brightlanecap.com</p>
  </section>

  <section class="card card--front" aria-label="Card front">
    <span class="name-tab"></span>
    <div class="person">
      <p class="person-name">Noah Keller</p>
      <p class="person-role">Founder</p>
    </div>

    <div class="brand-lockup"><span class="brand-dot"></span><span>Brightlane Capital</span></div>

    <p class="address">PO BOX 210 Elm Avenue<br>2nd street Ballarat</p>

    <ul class="contact-list">
      <li>
        <svg class="contact-icon" viewBox="0 0 26 26" aria-hidden="true">
          <circle cx="13" cy="13" r="12" fill="none" stroke="var(--brand-green)" stroke-width="2"/>
          <path d="M8 10c0-2 2-2 3-2l1 3-1.5 1c.6 1.5 1.5 2.4 3 3l1-1.5 3 1c0 1 0 3-2 3-4 0-7.5-3.5-7.5-7.5z" fill="var(--brand-green)"/>
        </svg>
        <span>(555) 318-2046</span>
      </li>
      <li>
        <svg class="contact-icon" viewBox="0 0 26 26" aria-hidden="true">
          <circle cx="13" cy="13" r="12" fill="none" stroke="var(--brand-green)" stroke-width="2"/>
          <rect x="7" y="9" width="12" height="8" fill="none" stroke="var(--brand-green)" stroke-width="1.6"/>
          <path d="M7 9l6 5 6-5" fill="none" stroke="var(--brand-green)" stroke-width="1.6"/>
        </svg>
        <span>info@brightlanecap.com</span>
      </li>
      <li>
        <svg class="contact-icon" viewBox="0 0 26 26" aria-hidden="true">
          <circle cx="13" cy="13" r="12" fill="none" stroke="var(--brand-green)" stroke-width="2"/>
          <circle cx="13" cy="13" r="6.5" fill="none" stroke="var(--brand-green)" stroke-width="1.4"/>
          <path d="M6.5 13h13M13 6.5c-3 3.5-3 9.5 0 13M13 6.5c3 3.5 3 9.5 0 13" fill="none" stroke="var(--brand-green)" stroke-width="1.2"/>
        </svg>
        <span>www.brightlanecap.com</span>
      </li>
    </ul>
  </section>
</body>
</html>
```